Book cover design for 'Lantern Winter' novel

Title of book 'Lantern Winter'
Subtitle 'a Ness Orford novel'
Author 'T K Halvorsen'
Book genre 'novel - adventure'
Format ' eBook, paperback, audio, thumbnail'
Type 'Self-publishing through PVL'
Trim size 6 x 9
Back cover 'Seeking redemption on the Via de la Plata.
Ness Orford’s life changed forever in a moment of madness. Haunted by his crime, Ness feels a calling to seek redemption on the Camino de Santiago.
The daily toil of walking the Via de la Plata from Seville causes Ness to search his soul.
On The Way Ness encounters other pilgrims with their own personal reasons to answer the call of the camino.
Join Ness for the many highs and lows of camino life as he moves step by step closer to his goal.
Can the Camino give Ness peace of mind and stop his nightmares?'
Overall vision 'The front cover at the top should be the title:
Camino
Calling
This will fill about 20 per cent of the front cover. It must be centre justified. The title should use the same type face as the official Camino de Santiago road sign (see first download). The type should be in bright blue. The background should be in bright yellow.
Under the title should be an image of a path stretching to the horizon with the shadow of a pilgrim (see second download).
Superimposed on the image should be the words 'a Ness Orford novel' maybe using a type face similar to the street signage used in Spain (see third download).
At the bottom of the front cover should be the author's name 'Tom Halvorsen' in the same style as the blue and yellow title - BUT MUCH SMALLER.
On the SPINE of the book should be 'Lantern Winter' and 'Tom Halvorsen' in the blue text on yellow background.
On the back cover there should be a photograph (see fourth download) with the text UPDATE ON THE TEXT 'Seeking redemption on the Via de la Plata.
In a moment of madness Ness Orford’s life changed forever. Haunted by his atrocious act, he feels a calling to seek redemption on the Camino de Santiago.
The daily slog of walking the Via de la Plata from Seville causes Ness to search deep within his soul.
On The Way Ness encounters other pilgrims with their own personal reasons to answer the call of the Camino.
Can the Camino give Ness peace of mind and stop his nightmares?' with a three centimetre space at the bottom for bar code/ISBN and the author headshot photograph attached.

Target Market(s)

Readers who have walked the Camino de Santiago in Spain or who are interested

Requirements
Nice to have
• I would like my headshot (attached) included on the back cover

```html
<!DOCTYPE html>
<html lang="en">
<head>
<meta charset="utf-8">
<title>Lantern Winter – Book Cover</title>
<link rel="stylesheet" href="https://fonts.googleapis.com/css2?family=Uncial+Antiqua&family=Roboto:ital,wght@0,400;0,900;1,900&family=Open+Sans:wght@400&display=swap">
<style>
  :root {
    --sign-yellow: #f1b925;
    --sign-blue: #0b6fc0;
    --rust-red: #a3331d;
    --body-ink: #2a2a24;
    --haze: #eef2df;
    --barcode-white: #ffffff;
  }
  html, body {
    margin: 0;
    padding: 0;
    overflow: hidden;
    background: #ddd;
  }
  .cover {
    position: relative;
    width: 1200px;
    height: 843px;
    overflow: hidden;
    font-family: "Open Sans", sans-serif;
  }
  /* Back cover */
  .back {
    position: absolute;
    left: 0; top: 0;
    width: 564px; height: 843px;
    overflow: hidden;
  }
  .back-photo {
    position: absolute; inset: 0;
    background:
      linear-gradient(180deg, var(--haze) 0%, #e8ecd6 28%, rgba(232,236,214,0) 45%),
      linear-gradient(90deg, #8a9a5a 0%, #a9ae72 30%, #c9a77a 60%, #d7b88e 100%);
  }
  .back-tagline {
    position: absolute;
    left: 66px; top: 80px;
    width: 452px;
    margin: 0;
    font-family: "Uncial Antiqua", serif;
    font-weight: 400;
    font-size: 14.6px;
    letter-spacing: 0;
    line-height: 20px;
    color: var(--rust-red);
    white-space: nowrap;
  }
  .back-blurb {
    position: absolute;
    left: 118px; top: 150px;
    width: 350px;
    margin: 0;
    font-size: 12px;
    line-height: 15.6px;
    color: var(--body-ink);
  }
  .back-blurb p { margin: 0; }
  .barcode-space {
    position: absolute;
    left: 363px; top: 697px;
    width: 160px; height: 105px;
    background: var(--barcode-white);
  }
  /* Spine */
  .spine {
    position: absolute;
    left: 564px; top: 0;
    width: 76px; height: 843px;
    background: var(--sign-yellow);
  }
  .spine-text {
    position: absolute;
    left: 50%;
    font-family: "Roboto", sans-serif;
    font-weight: 900;
    font-style: normal;
    color: var(--sign-blue);
    white-space: nowrap;
    transform-origin: left top;
    transform: rotate(90deg) translateY(-50%);
    line-height: 1;
  }
  .spine-title { top: 80px; font-size: 38px; }
  .spine-author { top: 604px; font-size: 30px; }
  /* Front cover */
  .front {
    position: absolute;
    left: 640px; top: 0;
    width: 560px; height: 843px;
  }
  .front-photo {
    position: absolute; inset: 0;
    background:
      linear-gradient(180deg, #8fb7e0 0%, #b5d0e8 30%, #6f8a3c 44%, #7ea23c 58%, #93b548 72%, #a89a62 88%, #b9986c 100%);
  }
  .title-panel {
    position: absolute;
    left: 29px; top: 50px;
    width: 497px; height: 200px;
    background: var(--sign-yellow);
    box-shadow: 3px 4px 8px rgba(0,0,0,0.35);
  }
  .title {
    position: absolute;
    left: 64px; top: 14px;
    margin: 0;
    font-family: "Roboto", sans-serif;
    font-weight: 900;
    font-style: normal;
    font-size: 86px;
    line-height: 78px;
    color: var(--sign-blue);
    letter-spacing: -1px;
  }
  .subtitle {
    position: absolute;
    left: 0; right: 0; top: 278px;
    margin: 0;
    text-align: center;
    font-family: "Uncial Antiqua", serif;
    font-size: 31px;
    color: var(--rust-red);
    text-shadow: 0 0 6px rgba(255,255,255,0.6);
    white-space: nowrap;
    padding-left: 20px;
  }
  .author-panel {
    position: absolute;
    left: 132px; top: 742px;
    width: 293px; height: 68px;
    background: var(--sign-yellow);
    display: flex;
    align-items: center;
    justify-content: center;
  }
  .author {
    font-family: "Roboto", sans-serif;
    font-weight: 900;
    font-style: italic;
    font-size: 33px;
    color: var(--sign-blue);
    white-space: nowrap;
  }
</style>
</head>
<body>
<div class="cover">
  <section class="back">
    <div class="back-photo" role="img" aria-label="Photograph of a dusty dirt trail through grass and wildflowers with a stone waymarker post for the Via de la Plata route"></div>
    <h2 class="back-tagline">SEEKING REDEMPTION ON THE VIA DE LA PLATA</h2>
    <div class="back-blurb">
      <p>Ness Orford’s life changed forever in a moment of madness. Haunted by his crime, Ness feels a calling to seek redemption on the Camino de Santiago.</p>
      <p>The daily toil of walking the Via de la Plata from Seville causes Ness to search his soul.</p>
      <p>On The Way Ness encounters other pilgrims with their own personal reasons to answer the call of the camino.</p>
      <p>Join Ness for the many highs and lows of camino life as he moves step by step closer to his goal.</p>
      <p>Can the Camino give Ness peace of mind and stop his nightmares?</p>
    </div>
    <div class="barcode-space"></div>
  </section>

  <section class="spine">
    <span class="spine-text spine-title">Lantern Winter</span>
    <span class="spine-text spine-author">T K Halvorsen</span>
  </section>

  <section class="front">
    <div class="front-photo" role="img" aria-label="Photograph of a country path stretching toward the horizon under oak trees, with the long shadow of a pilgrim on the grass"></div>
    <div class="title-panel">
      <h1 class="title">Lantern<br>Winter</h1>
    </div>
    <p class="subtitle">A NESS ORFORD NOVEL</p>
    <div class="author-panel">
      <span class="author">T K Halvorsen</span>
    </div>
  </section>
</div>
</body>
</html>
```